Quorvel Landing page redesign

We are looking for a landing page redesign before we officially launch. We want to incorporate the information already on the site at www.Quorvel-example.com landing page but make it more inviting. There needs to be a sign up section along with clearly stating what we do. Having a place for sample profiles and linking to our blog and podcast is option. More information about all we will be doing is at Quorvel is on the landing page and also on the blog.

Target Market(s)

35 years old and up.

Coding

Coded - Design and coding required

Number of Pages Required

1 page

Requirements
Must have
• The top bar and the bottom bar (with the privacy policy, etc)
• Sign in/up section.
• I don't want to give to much here because I want designers to be creative.
Nice to have
• Prefer not to have a landing page that requires a lot of scrolling at all.

```html
<!DOCTYPE html>
<html lang="en">
<head>
<meta charset="utf-8">
<title>Quorvel</title>
<link rel="stylesheet" href="https://fonts.googleapis.com/css2?family=Raleway:wght@300;400;500;600;700;800&family=Open+Sans:wght@400;600;700&display=swap">
<style>
:root{
  --navy:#1b1d5f;
  --navy-deep:#191a57;
  --purple:#7c3a97;
  --ink:#222;
  --paper:#fbf8f9;
  --mist:#e9e9ef;
  --field:#fbf6b6;
  --panel-grey:#e4e4e6;
  --line:#cfcfd6;
  --white:#fff;
}
*{box-sizing:border-box;margin:0;padding:0}
html,body{width:1200px;height:2812px;overflow:hidden}
body{position:relative;font-family:"Open Sans",Arial,sans-serif;color:var(--ink);background:var(--white)}
.abs{position:absolute}

/* top bar */
.topbar{left:0;top:0;width:1200px;height:75px;background:var(--white)}
.brand{display:flex;align-items:center;font-family:"Raleway",sans-serif;color:var(--navy);font-size:25px;font-weight:600;letter-spacing:.5px}
.topbar .brand{left:165px;top:20px}
.login{left:885px;top:25px;font:700 16px "Raleway",sans-serif;color:var(--ink)}
.signup{left:940px;top:22px;width:96px;height:31px;border-radius:16px;background:var(--navy);color:var(--white);font:700 15px "Raleway",sans-serif;display:flex;align-items:center;justify-content:center}

/* hero */
.hero{left:0;top:75px;width:1200px;height:519px;background:linear-gradient(100deg,#242466 0%,#4b2f85 50%,#7e3a98 100%)}
.hero-title{left:0;top:198px;width:1200px;text-align:center;color:var(--white);font:800 26px "Raleway",sans-serif;letter-spacing:.3px}
.hero-sub{left:0;top:234px;width:1200px;text-align:center;color:var(--white);font:400 19px "Raleway",sans-serif}
.hero-kicker{left:0;top:309px;width:1200px;text-align:center;color:var(--white);font:700 15px "Raleway",sans-serif;letter-spacing:.3px}
.hero-cta{left:488px;top:358px;width:224px;height:43px;border-radius:22px;background:var(--white);color:var(--navy-deep);font:600 15px "Raleway",sans-serif;display:flex;align-items:center;justify-content:center}

/* feature bands */
.band{left:0;width:1200px}
.band-one{top:594px;height:512px;background:var(--paper)}
.band-two{top:1106px;height:447px;background:var(--mist)}
.band-three{top:1553px;height:478px;background:var(--white)}
.feature-num{font:300 58px "Raleway",sans-serif;color:var(--purple);line-height:1}
.feature-title{font:500 18px "Raleway",sans-serif;color:#333;white-space:nowrap}
.feature-copy{font:400 9.5px/15px Arial,Helvetica,sans-serif;color:#444;width:295px}

/* product panel mockups */
.mock{position:absolute;font-size:9px;color:#333}
.mock-bar{position:absolute;left:0;top:0;right:0;height:22px;background:var(--navy);color:var(--white);font:700 11px "Open Sans",sans-serif;text-align:center;line-height:22px}
.mock-bar .close{position:absolute;right:10px;top:0;font-weight:400}
.mock-bar .lock{position:absolute;left:8px;top:6px;width:9px;height:9px;background:#d8324b;border-radius:2px}
.mock-sheet{position:absolute;background:var(--white);box-shadow:0 1px 4px rgba(0,0,0,.25)}
.mock-tray{position:absolute;background:var(--panel-grey)}
.tag-yellow{position:absolute;background:var(--field);font:700 10px "Open Sans",sans-serif;color:var(--navy);padding:3px 6px}
.mini-label{position:absolute;font-weight:700;font-size:7.5px;color:#222;white-space:nowrap}
.mini-field{position:absolute;height:13px;background:var(--field)}
.mini-actions{position:absolute;font-weight:700;font-size:8px;color:#333;white-space:nowrap}
.swatches{position:absolute;display:flex;gap:3px}
.swatches span{width:13px;height:13px;display:block}
.swatches.small{gap:2px}
.swatches.small span{width:11px;height:11px}
.btn-cancel,.btn-save{position:absolute;color:var(--white);font-weight:700;font-size:8px;display:flex;align-items:center;justify-content:center}
.btn-cancel{background:#2b2b2b}
.btn-save{background:var(--navy)}
.check{position:absolute;font-size:8px;display:flex;align-items:center;gap:4px;white-space:nowrap}
.check i{width:8px;height:8px;background:#3a7bd5;border-radius:2px;display:block}
.photo{position:absolute}
.add-media{position:absolute;border:1px solid #999;background:#ececec;font-weight:700;font-size:8px;display:flex;align-items:center;justify-content:center}
.tray-title{position:absolute;font-weight:700;font-size:8px}

/* early user */
.early{left:0;top:2031px;width:1200px;height:463px;background:linear-gradient(100deg,#2a2a6c 0%,#4f3088 50%,#823c9a 100%)}
.early-title{left:0;top:2066px;width:1200px;text-align:center;color:var(--white);font:800 22px "Raleway",sans-serif}
.form-label{left:384px;color:var(--white);font:700 12px "Open Sans",sans-serif}
.form-field{left:384px;width:432px;height:35px;background:rgba(255,255,255,.18);border:1px solid rgba(255,255,255,.25);color:var(--white);font-size:13px;display:flex;align-items:center;padding-left:30px}
.form-field svg{position:absolute;left:8px;top:8px}
.subscribe{left:383px;top:2360px;width:138px;height:34px;background:var(--white);border:2px solid #222;font:700 13px "Open Sans",sans-serif;color:#111;display:flex;align-items:center;justify-content:center;letter-spacing:.5px}
.already{left:383px;top:2405px;color:var(--white);font-size:12px}
.already a{color:var(--navy);font-weight:600;text-decoration:none}

/* resources strip */
.resources{left:0;top:2494px;width:1200px;height:187px;background:var(--white)}
.resources-divider{left:600px;top:2494px;width:1px;height:187px;background:#ddd}
.resource-label{font:600 13px "Open Sans",sans-serif;color:#222;text-align:center;width:100px}
.news-title{left:662px;top:2514px;font:600 14px "Raleway",sans-serif;font-variant:small-caps;color:#222;letter-spacing:.3px}
.news-input{left:662px;top:2546px;width:266px;height:36px;border:1px solid #ccc;font-size:12px;color:#999;display:flex;align-items:center;padding-left:10px}
.news-send{left:927px;top:2546px;width:42px;height:36px;border:1px solid #ccc;display:flex;align-items:center;justify-content:center}
.connect{left:662px;top:2597px;font:600 12px "Open Sans",sans-serif;color:#222}
.social{top:2624px;width:32px;height:32px;border-radius:50%;background:#c8c8cf}

/* bottom bar */
.bottombar{left:0;top:2681px;width:1200px;height:131px;background:var(--navy-deep)}
.footer-brand{left:165px;top:2730px;color:var(--white)}
.legal{right:157px;top:2741px;color:var(--white);font-size:11px}
</style>
</head>
<body>

<header class="abs topbar">
  <div class="abs brand">Quorvel</div>
  <a class="abs login">Log in</a>
  <a class="abs signup">Sign up</a>
</header>

<section class="abs hero" role="img" aria-label="Faded family photos pinned to a wall behind a navy to purple tint"></section>
<h1 class="abs hero-title">WE ARE JUST TRYING TO CUPTURE THE MOMENT AS THE BEST WAY</h1>
<p class="abs hero-sub">Bring here more memories and joy and we will do good care of it</p>
<p class="abs hero-kicker">START A SAFE AND SECURE JOURNEY WITH US</p>
<a class="abs hero-cta">Create your free account</a>

<!-- feature 01 -->
<section class="abs band band-one"></section>
<div class="abs feature-num" style="left:160px;top:722px">01</div>
<h2 class="abs feature-title" style="left:229px;top:764px">Create Timelines, Maps, Family Trees</h2>
<p class="abs feature-copy" style="left:229px;top:797px">Lorem ipsum dolor sit amet, consectetur adipiscing elit. Proin in lobortis arcu. Nunc vitae neque a purus commodo blandit. Aenean odio est, vulputate vel justo a, dapibus pellentesque lacus. Etiam elementum rhoncus nunc, eu varius ipsum vehicula nec. Pellentesque hendrerit arcu eu tristique rutrum. Morbi</p>

<div class="mock" style="left:592px;top:636px;width:447px;height:418px">
  <div class="mock-tray" style="left:10px;top:236px;width:427px;height:182px"></div>
  <div class="mock-sheet" style="left:10px;top:0;width:427px;height:246px"></div>
  <div class="mock-bar" style="left:0;width:447px">My Life<span class="close">✕</span></div>
  <div class="abs" style="left:22px;top:38px;font-weight:700;font-size:9px">HISTORICAL EVENT: <span style="font-weight:400">September 11 Attacks</span></div>
  <div class="mini-actions" style="left:266px;top:38px">EDIT ✎ &nbsp;&nbsp;<span style="color:#bbb">SHARE ⇪</span>&nbsp;&nbsp; DELETE 🗑</div>
  <div class="abs" style="left:10px;top:52px;width:427px;height:1px;background:var(--line)"></div>
  <div class="photo" role="img" aria-label="Memorial poster for the historical event" style="left:27px;top:54px;width:99px;height:135px;background:linear-gradient(160deg,#2a2a2a,#111 60%,#5a1f1f)"></div>
  <div class="mini-label" style="left:136px;top:64px">Date</div>
  <div class="abs" style="left:136px;top:74px;font-size:10px">September 11, 2001</div>
  <div class="mini-label" style="left:283px;top:64px">Location</div>
  <div class="abs" style="left:283px;top:74px;font-size:10px">United States</div>
  <div class="mini-label" style="left:136px;top:98px">Description</div>
  <div class="abs" style="left:136px;top:108px;width:280px;font-size:10px;color:#555;line-height:13px">Where were you when you found out? What were your emotions?</div>
  <div class="abs" style="left:146px;top:148px;font-size:7px;color:var(--navy);text-decoration:underline">Record your video or audio account of that day</div>
  <div class="mini-label" style="left:150px;top:174px;font-size:8px">EVENT COLOR</div>
  <div class="swatches" style="left:245px;top:171px"><span style="background:#e52b2b"></span><span style="background:#f28a1b"></span><span style="background:#f3e21a"></span><span style="background:#36a43a"></span><span style="background:#1a3fd8"></span><span style="background:var(--navy)"></span><span style="background:#7a2a8e"></span><span style="background:#a8232e"></span><span style="background:#111"></span></div>
  <div class="btn-cancel" style="left:235px;top:194px;width:78px;height:34px">CANCEL</div>
  <div class="btn-save" style="left:318px;top:194px;width:107px;height:34px">SAVE CHANGES</div>
  <div class="check" style="left:22px;top:232px"><span>Commenting Enabled</span><i></i></div>
  <div class="photo" role="img" aria-label="Commenter avatar" style="left:38px;top:258px;width:24px;height:24px;background:#8b8f9a"></div>
  <div class="abs" style="left:70px;top:256px;width:340px;font-size:6.5px;line-height:9px"><b style="color:var(--navy)">Milo Brandt</b><br>I remember the morning clearly, we all gathered around the radio at work and nobody spoke for a long time.</div>
  <div class="photo" role="img" aria-label="Commenter avatar" style="left:38px;top:304px;width:24px;height:24px;background:#9a8f84"></div>
  <div class="abs" style="left:70px;top:302px;width:340px;font-size:6.5px;line-height:9px"><b style="color:var(--navy)">Ines Carrow</b><br>My father called from overseas to make sure we were safe, a call I still think about every single year.</div>
  <div class="photo" role="img" aria-label="User avatar" style="left:38px;top:358px;width:22px;height:22px;background:#555"></div>
  <div class="abs" style="left:64px;top:360px;width:220px;height:18px;background:var(--white);font-size:7px;padding:4px 0 0 150px">Attach Media</div>
  <div class="btn-save" style="left:290px;top:358px;width:88px;height:22px">SHARE STORY</div>
</div>

<!-- feature 02 -->
<section class="abs band band-two"></section>
<div class="mock" style="left:156px;top:1149px;width:442px;height:362px">
  <div class="mock-tray" style="left:0;top:244px;width:442px;height:118px;background:#d6d6d9"></div>
  <div class="mock-sheet" style="left:10px;top:10px;width:422px;height:234px;box-shadow:none"></div>
  <div class="mock-bar" style="height:20px;line-height:20px;font-size:9px"><span class="lock"></span>MY LIFE<span class="close">✕</span></div>
  <div class="abs" style="left:0;top:20px;width:12px;height:210px;background:var(--navy)"></div>
  <div class="abs" style="left:430px;top:20px;width:12px;height:210px;background:var(--navy)"></div>
  <div class="tag-yellow" style="left:18px;top:30px;width:130px">5 YEAR CHECK UP</div>
  <div class="abs" style="left:165px;top:30px;width:110px;height:14px;border:1px solid var(--navy);font-size:7px;font-weight:700;padding:1px 4px">GROWTH CHART ▾</div>
  <div class="mini-actions" style="left:325px;top:32px;font-size:7px">EDIT ✎ &nbsp;<span style="color:#bbb">SHARE</span>&nbsp; DELETE 🗑</div>
  <div class="photo" role="img" aria-label="Portrait of a young child in a red shirt" style="left:18px;top:64px;width:139px;height:133px;background:linear-gradient(170deg,#b8d4e4,#d89a8a 55%,#c63b46)"></div>
  <div class="mini-label" style="left:165px;top:50px">Date</div>
  <div class="mini-field" style="left:165px;top:60px;width:110px;font-size:6px;padding:2px 4px">June 20th, 2016</div>
  <div class="mini-label" style="left:165px;top:84px">Height</div><div class="mini-field" style="left:165px;top:94px;width:55px"></div>
  <div class="mini-label" style="left:225px;top:84px">Height %</div><div class="mini-field" style="left:225px;top:94px;width:55px"></div>
  <div class="mini-label" style="left:285px;top:84px">Weight</div><div class="mini-field" style="left:285px;top:94px;width:55px"></div>
  <div class="mini-label" style="left:345px;top:84px">Weight %</div><div class="mini-field" style="left:345px;top:94px;width:55px"></div>
  <div class="mini-label" style="left:225px;top:118px">Head Circumference</div><div class="mini-field" style="left:225px;top:128px;width:80px"></div>
  <div class="mini-label" style="left:320px;top:118px">Head Circumference %</div><div class="mini-field" style="left:320px;top:128px;width:80px"></div>
  <div class="mini-label" style="left:165px;top:150px">Comments</div>
  <div class="mini-field" style="left:165px;top:160px;width:250px;height:22px"></div>
  <div class="mini-label" style="left:228px;top:192px;font-size:7px">EVENT COLOR</div>
  <div class="swatches small" style="left:288px;top:190px"><span style="background:#e52b2b"></span><span style="background:#f28a1b"></span><span style="background:#f3e21a"></span><span style="background:#36a43a"></span><span style="background:#1a3fd8"></span><span style="background:var(--navy)"></span><span style="background:#7a2a8e"></span><span style="background:#a8232e"></span><span style="background:#111"></span></div>
  <div class="btn-cancel" style="left:230px;top:206px;width:56px;height:24px;font-size:7px">CANCEL</div>
  <div class="btn-save" style="left:292px;top:206px;width:80px;height:24px;font-size:7px">SAVE CHANGES</div>
  <div class="check" style="left:164px;top:232px;font-size:7px"><span>Commenting Enabled</span><i></i></div>
  <div class="tray-title" style="left:12px;top:252px">MEDIA</div>
  <div class="add-media" style="left:12px;top:282px;width:75px;height:72px">ADD MEDIA</div>
  <div class="photo" role="img" aria-label="Child playing outdoors" style="left:96px;top:282px;width:75px;height:72px;background:linear-gradient(160deg,#9fbfd6,#c9a98c)"></div>
  <div class="photo" role="img" aria-label="Child at a celebration" style="left:178px;top:282px;width:75px;height:72px;background:linear-gradient(160deg,#4d6fa6,#d7c0a6)"></div>
  <div class="photo" role="img" aria-label="Baby portrait" style="left:260px;top:282px;width:75px;height:72px;background:linear-gradient(160deg,#3b3431,#a07c64)"></div>
  <div class="photo" role="img" aria-label="Newborn with parent" style="left:342px;top:282px;width:75px;height:72px;background:linear-gradient(160deg,#c9b5a4,#7a6a62)"></div>
</div>
<div class="abs feature-num" style="left:660px;top:1202px">02</div>
<h2 class="abs feature-title" style="left:731px;top:1245px">Share Family Stories, History and more</h2>
<p class="abs feature-copy" style="left:731px;top:1278px">Lorem ipsum dolor sit amet, consectetur adipiscing elit. Proin in lobortis arcu. Nunc vitae neque a purus commodo blandit. Aenean odio est, vulputate vel justo a, dapibus pellentesque lacus. Etiam elementum rhoncus nunc, eu varius ipsum vehicula nec. Pellentesque hendrerit arcu eu tristique rutrum. Morbi</p>

<!-- feature 03 -->
<section class="abs band band-three"></section>
<div class="abs feature-num" style="left:160px;top:1666px">03</div>
<h2 class="abs feature-title" style="left:229px;top:1707px">Memorialize Loved Ones</h2>
<p class="abs feature-copy" style="left:229px;top:1740px">Lorem ipsum dolor sit amet, consectetur adipiscing elit. Proin in lobortis arcu. Nunc vitae neque a purus commodo blandit. Aenean odio est, vulputate vel justo a, dapibus pellentesque lacus. Etiam elementum rhoncus nunc, eu varius ipsum vehicula nec. Pellentesque hendrerit arcu eu tristique rutrum. Morbi</p>

<div class="mock" style="left:602px;top:1597px;width:439px;height:387px">
  <div class="mock-tray" style="left:0;top:268px;width:439px;height:119px;background:#d6d6d9"></div>
  <div class="mock-sheet" style="left:10px;top:10px;width:419px;height:258px;box-shadow:none"></div>
  <div class="mock-bar" style="height:20px;line-height:20px;font-size:10px"><span class="lock"></span>SPORTS<span class="close">✕</span></div>
  <div class="abs" style="left:0;top:20px;width:12px;height:210px;background:var(--navy)"></div>
  <div class="abs" style="left:427px;top:20px;width:12px;height:210px;background:var(--navy)"></div>
  <div class="tag-yellow" style="left:18px;top:30px;width:137px">SUMMER GOLF TRIP</div>
  <div class="mini-actions" style="left:330px;top:30px;font-size:7px">EDIT ✎ &nbsp;<span style="color:#bbb">SHARE</span>&nbsp; DELETE 🗑</div>
  <div class="photo" role="img" aria-label="Golf course green under a blue sky" style="left:18px;top:53px;width:137px;height:141px;background:linear-gradient(180deg,#3f7fc2 0%,#7fb6e0 45%,#3f7a36 60%,#2f5e2a 100%)"></div>
  <div class="mini-label" style="left:163px;top:45px">Date</div>
  <div class="mini-field" style="left:163px;top:55px;width:120px;font-size:6px;padding:2px 4px">June 20th, 2016</div>
  <div class="mini-label" style="left:295px;top:45px">Location</div><div class="mini-field" style="left:295px;top:55px;width:120px"></div>
  <div class="mini-label" style="left:163px;top:78px">Course</div><div class="mini-field" style="left:163px;top:88px;width:80px"></div>
  <div class="mini-label" style="left:252px;top:78px">Total Par/Yardage</div><div class="mini-field" style="left:252px;top:88px;width:80px"></div>
  <div class="mini-label" style="left:340px;top:78px">Tees Played</div><div class="mini-field" style="left:340px;top:88px;width:75px"></div>
  <div class="mini-label" style="left:163px;top:108px">Total Strokes</div><div class="mini-field" style="left:163px;top:118px;width:80px"></div>
  <div class="mini-label" style="left:295px;top:108px">Golf Partners</div><div class="mini-field" style="left:295px;top:118px;width:120px"></div>
  <div class="mini-label" style="left:163px;top:138px">Comments</div>
  <div class="mini-field" style="left:163px;top:148px;width:252px;height:34px"></div>
  <div class="mini-label" style="left:225px;top:193px;font-size:7px">EVENT COLOR</div>
  <div class="swatches small" style="left:285px;top:190px"><span style="background:#e52b2b"></span><span style="background:#f28a1b"></span><span style="background:#f3e21a"></span><span style="background:#36a43a"></span><span style="background:#1a3fd8"></span><span style="background:var(--navy)"></span><span style="background:#7a2a8e"></span><span style="background:#a8232e"></span><span style="background:#111"></span></div>
  <div class="btn-cancel" style="left:285px;top:210px;width:54px;height:26px;font-size:7px">CANCEL</div>
  <div class="btn-save" style="left:345px;top:210px;width:80px;height:26px;font-size:7px">SAVE CHANGES</div>
  <div class="check" style="left:163px;top:240px;font-size:7px"><span>Commenting Enabled</span><i></i></div>
  <div class="tray-title" style="left:12px;top:276px">MEDIA</div>
  <div class="add-media" style="left:12px;top:305px;width:75px;height:72px">ADD MEDIA</div>
  <div class="photo" role="img" aria-label="Golf ball on the fairway" style="left:95px;top:305px;width:75px;height:72px;background:linear-gradient(160deg,#7ea25a,#3d6b2a)"></div>
  <div class="photo" role="img" aria-label="Golf clubs in a bag" style="left:178px;top:305px;width:75px;height:72px;background:linear-gradient(160deg,#2b2b2b,#777)"></div>
  <div class="photo" role="img" aria-label="Golf ball at night" style="left:261px;top:305px;width:75px;height:72px;background:linear-gradient(160deg,#1b1b1b,#6b4a2a)"></div>
  <div class="photo" role="img" aria-label="Golf course landscape" style="left:344px;top:305px;width:75px;height:72px;background:linear-gradient(180deg,#5fa0d8,#4e8c3a)"></div>
</div>

<!-- early user -->
<section class="abs early" role="img" aria-label="Soft family scene behind a navy to purple tint"></section>
<h2 class="abs early-title">BECOME AN EARLY USER</h2>
<label class="abs form-label" style="top:2135px">YOUR NAME</label>
<div class="abs form-field" style="top:2157px">
  <svg width="18" height="18" viewBox="0 0 18 18" fill="none" stroke="rgba(255,255,255,.7)" stroke-width="1.5"><path d="M3 13l8-8 3 3-8 8H3z"/><path d="M10 6l3 3"/></svg>
</div>
<label class="abs form-label" style="top:2210px">YOUR EMAIL ADDRESS</label>
<div class="abs form-field" style="top:2232px">
  <svg width="18" height="18" viewBox="0 0 18 18" fill="none" stroke="rgba(255,255,255,.7)" stroke-width="1.5"><rect x="2" y="4" width="14" height="10"/><path d="M2 4l7 6 7-6"/></svg>
</div>
<label class="abs form-label" style="top:2286px">DATE OF BIRTH</label>
<div class="abs form-field" style="top:2306px;padding-left:14px">20/01/2017
  <svg style="left:auto;right:10px" width="18" height="18" viewBox="0 0 18 18" fill="none" stroke="rgba(255,255,255,.7)" stroke-width="1.5"><rect x="2" y="3" width="14" height="13"/><path d="M2 7h14M6 10h2M10 10h2M6 13h2M10 13h2"/></svg>
</div>
<a class="abs subscribe">SUBSCRIBE</a>
<p class="abs already">Already Have an Account? <a>Sign In</a></p>

<!-- resources -->
<section class="abs resources"></section>
<div class="abs resources-divider"></div>
<svg class="abs" style="left:258px;top:2550px" width="54" height="54" viewBox="0 0 54 54" fill="none" stroke="var(--navy)" stroke-width="5"><path d="M30 6H6v42h42V24"/><path d="M44 4l6 6-22 22h-6v-6z" fill="var(--navy)"/></svg>
<div class="abs resource-label" style="left:235px;top:2615px">Blog</div>
<svg class="abs" style="left:390px;top:2536px" width="48" height="70" viewBox="0 0 48 70" fill="var(--navy)"><rect x="12" y="2" width="24" height="40" rx="12"/><path d="M4 30a20 20 0 0040 0" fill="none" stroke="var(--navy)" stroke-width="5"/><rect x="21" y="50" width="6" height="12"/><rect x="10" y="62" width="28" height="6"/></svg>
<div class="abs resource-label" style="left:364px;top:2615px">Podcast</div>

<h3 class="abs news-title">Newsletter Subscription</h3>
<div class="abs news-input">E-mail address</div>
<div class="abs news-send"><svg width="20" height="20" viewBox="0 0 20 20" fill="var(--navy)"><path d="M1 9L19 1l-6 18-3-7z"/></svg></div>
<p class="abs connect">Connect with us through</p>
<span class="abs social" style="left:662px"></span>
<span class="abs social" style="left:701px"></span>
<span class="abs social" style="left:740px"></span>
<span class="abs social" style="left:779px"></span>

<!-- bottom bar -->
<footer class="abs bottombar"></footer>
<div class="abs brand footer-brand">Quorvel</div>
<p class="abs legal">Privacy Policy | Terms of Use | Data Tracking Policy | Submit Feedback | Quorvel © 2017</p>

</body>
</html>
```